website re-design - the brisk loft

The Brisk Loft is an existing website that we built using a new zealand based online CMS tool which is quite flexible and accomodates custom designs. You can check it here: http://www.pagecrafter.co.nz/.

We have a logo already and the content on the website is OK.
The website can be found at www.thebriskloft.com.au

mainly the homepage, but if the design is easily adapted to the other pages then, we will commission the winner to update these pages also.
Updates

Hi there,  I am uploading an image to be used as the main image on the homepage design,  so all submissions have the same image.

Target Market(s)

property developers, architects, builders, home buyers

Industry/Entity Type

Shop

Requirements
Must have
• Must utilise the existing CMS or at least be compatible to upload
Nice to have
• a promotional banner that can be turned off and on and changed as required as we offer different promotions over time.

```html
<!DOCTYPE html>
<html lang="en">
<head>
<meta charset="utf-8">
<title>The Brisk Loft – Contact</title>
<link rel="stylesheet" href="https://fonts.googleapis.com/css2?family=Roboto:ital,wght@0,300;0,400;0,500;1,300&family=Oswald:wght@500;700&display=swap">
<style>
:root{
  --sidebar:#2b2b2b;
  --sidebar-dark:#1c1c1c;
  --panel:#e6e6e6;
  --orange:#f07b0c;
  --orange-light:#ff9a1e;
  --text-dark:#2a2a2a;
  --text-mid:#555;
  --text-light:#cfcfcf;
  --text-muted:#8a8a8a;
  --blue:#1a8ef0;
  --blue-light:#3fb4ff;
  --field:#f7f7f7;
  --field-border:#cfcfcf;
}
*{box-sizing:border-box;margin:0;padding:0}
html,body{width:857px;height:1200px;overflow:hidden}
body{position:relative;background:var(--sidebar);font-family:"Roboto",Arial,sans-serif;color:var(--text-dark)}
.abs{position:absolute}
.main-panel{left:254px;top:0;width:603px;height:1135px;background:var(--panel);border-bottom-left-radius:16px}
.footer{left:0;top:1135px;width:857px;height:65px;background:var(--sidebar)}

/* header */
.brand-mark{left:276px;top:36px;width:48px;height:48px;border:4px solid var(--orange)}
.brand-name{left:336px;top:42px;font-size:24px;font-weight:400;color:var(--text-dark);letter-spacing:.5px}
.brand-sub{left:412px;top:73px;font-size:11.5px;color:var(--orange);letter-spacing:1px}

/* nav */
.site-tab{left:27px;top:119px;width:227px;height:33px;background:linear-gradient(#ff9b28,#e56d07);border-radius:6px 0 0 6px;box-shadow:0 4px 6px rgba(0,0,0,.5)}
.site-tab span{position:absolute;left:38px;top:5px;font-family:"Oswald",sans-serif;font-weight:700;font-size:18px;color:#3a1d05;letter-spacing:-.3px}
.main-nav{left:254px;top:119px;width:577px;height:33px;background:linear-gradient(#4a4a4a,#262626);border-radius:0 6px 6px 0;box-shadow:0 4px 6px rgba(0,0,0,.45);display:flex;align-items:center;padding-left:10px;gap:0}
.main-nav a{font-size:10.5px;color:#e2e2e2;text-decoration:none;padding:5px 7px;border-radius:3px;margin-right:3px}
.main-nav a.active{background:#151515;color:var(--orange-light);box-shadow:inset 0 0 0 1px #444}

/* sidebar */
.search{left:56px;top:169px;width:188px;height:22px;background:#1d1d1d;border:1px solid #3a3a3a}
.search span{position:absolute;left:7px;top:4px;font-size:10px;color:#9a9a9a;letter-spacing:.3px}
.search-btn{left:218px;top:169px;width:26px;height:22px;background:var(--orange)}
.tagline{right:613px;top:218px;text-align:right;font-weight:300;font-size:20px;line-height:25px;color:#9c9c9c}
.tagline .strong{color:#e8e8e8;font-size:22px;line-height:31px}
.divider{height:0;border-top:1px dotted #777}
.promo{left:32px;top:408px;width:209px;height:251px;background:#6b6b6b;border-radius:6px;padding:8px}
.promo-inner{width:100%;height:100%;background:linear-gradient(#101010 0,#3c3c3c 45%,#111 45%,#3a3a3a 100%);border-radius:6px;border:1px solid #000;text-align:center;color:#fff;font-family:"Oswald",sans-serif}
.promo-pct{font-size:82px;font-weight:700;line-height:1;padding-top:18px;background:linear-gradient(#ffae2b,#e06200);-webkit-background-clip:text;background-clip:text;color:transparent;letter-spacing:-3px}
.promo-text{font-size:17px;font-weight:500;line-height:17px;margin-top:17px;letter-spacing:.5px}
.promo-date{font-size:19px;font-weight:500;margin-top:11px;letter-spacing:.5px}
.side-heading{right:613px;font-weight:300;font-size:18px;color:var(--orange-light);letter-spacing:-.5px}
.side-input{left:56px;width:188px;height:22px;background:#1d1d1d;border:1px solid #3a3a3a}
.side-input span{position:absolute;left:3px;top:4px;font-size:10px;color:#aaa}
.btn-blue{background:linear-gradient(var(--blue-light),var(--blue));border-radius:2px;font-family:"Oswald",sans-serif;font-weight:700;font-size:12px;color:#06305a;text-align:center;line-height:25px;letter-spacing:.3px}
.quote{right:613px;top:926px;width:200px;text-align:right;font-style:italic;font-weight:300;font-size:13px;line-height:16px;color:#d0d0d0}
.quote-author{right:613px;top:1012px;font-weight:300;font-size:13px;color:#777}

/* content */
.content-line{left:269px;width:549px;border-top:1px dotted #999}
.page-title{left:272px;top:182px;font-size:22px;font-weight:500;color:var(--text-dark)}
.page-title em{font-style:normal;font-weight:400;color:var(--orange)}
.post-meta{right:45px;top:193px;font-size:10.5px;color:var(--text-dark)}
.post-meta b{font-weight:400;color:var(--orange)}
.region-map{left:272px;top:233px;width:264px;height:240px;background:radial-gradient(ellipse at 50% 45%,#d0d0d0 0,#dcdcdc 50%,rgba(230,230,230,0) 72%)}
.contact-card{left:554px;top:259px;width:265px;height:126px;background:linear-gradient(#141414,#3a3a3a);border-radius:7px;padding:12px 15px;color:#d4d4d4;font-size:11px;line-height:14px}
.contact-card dl{display:grid;grid-template-columns:56px 1fr}
.contact-card dd::before{content:": "}
.contact-card .wrap{padding-left:8px}
.contact-card .wrap::before{content:""}
.gap{margin-top:3px}
.form-label{right:491px;font-size:10.5px;color:var(--text-mid)}
.form-field{left:378px;width:397px;height:24px;background:linear-gradient(#fff,#ececec);border:1px solid var(--field-border);border-radius:2px}
.form-message{left:378px;top:642px;width:395px;height:122px;background:linear-gradient(#fff,#eaeaea);border:1px solid var(--field-border);border-radius:2px}
.form-message span{position:absolute;left:9px;top:9px;font-size:10px;color:#555}

/* footer */
.social-icon{top:1151px;width:28px;height:28px;background:linear-gradient(#eee,#a9a9a9);border-radius:4px;box-shadow:inset 0 0 0 2px #777}
.copyright{right:26px;top:1159px;font-size:10px;color:#9a9a9a}
</style>
</head>
<body>
<div class="abs main-panel"></div>
<div class="abs footer"></div>

<header>
  <div class="abs brand-mark"></div>
  <div class="abs brand-name">The Brisk Loft</div>
  <div class="abs brand-sub">ARCHITECTURAL SCALE MODELS</div>
</header>

<div class="abs site-tab"><span>THE BRISK LOFT</span></div>
<nav class="abs main-nav">
  <a>Home</a><a>Gallery</a><a>Order Online</a><a>Get a Quote</a><a class="active">Contact</a><a>3D Visualitation</a><a>About Us</a><a>Sitemap</a>
</nav>

<aside>
  <div class="abs search"><span>search</span></div>
  <div class="abs search-btn">
    <svg width="26" height="22" viewBox="0 0 26 22"><circle cx="11" cy="9" r="5" fill="none" stroke="#fff" stroke-width="2"/><line x1="15" y1="13" x2="20" y2="18" stroke="#fff" stroke-width="2.6" stroke-linecap="round"/></svg>
  </div>
  <p class="abs tagline">A picture may be<br>worth a thousand<br>words, but<br><span class="strong">a model says it all</span></p>
  <div class="abs divider" style="left:40px;top:352px;width:204px"></div>

  <div class="abs promo">
    <div class="promo-inner">
      <div class="promo-pct">20%</div>
      <div class="promo-text">Off all models<br>ordered before</div>
      <div class="promo-date">31st December 2011</div>
    </div>
  </div>

  <div class="abs divider" style="left:40px;top:690px;width:204px"></div>
  <h3 class="abs side-heading" style="top:713px">NEWSLETTER</h3>
  <div class="abs side-input" style="top:740px"><span>Your name</span></div>
  <div class="abs side-input" style="top:776px"><span>Email</span></div>
  <div class="abs btn-blue" style="left:162px;top:809px;width:80px;height:25px">SUBSCRIBE</div>

  <div class="abs divider" style="left:40px;top:864px;width:204px"></div>
  <h3 class="abs side-heading" style="top:889px">TESTIMONIALS</h3>
  <p class="abs quote">“Nice work, great detail.<br>Here...You can tailor your model<br>to suit your project and budget<br>needs”</p>
  <p class="abs quote-author">- Sam Keller -</p>
  <div class="abs btn-blue" style="left:162px;top:1039px;width:80px;height:25px">READ MORE</div>
</aside>

<main>
  <div class="abs content-line" style="top:176px"></div>
  <h1 class="abs page-title"><em>BL</em>Contact</h1>
  <p class="abs post-meta">Added <b>Nov 28, 2011</b> By <b>Admin</b></p>
  <div class="abs content-line" style="top:216px"></div>

  <div class="abs region-map" role="img" aria-label="Faint outline map of Australia with a dotted grid over the western region"></div>

  <div class="abs contact-card">
    <dl>
      <dt>Contact</dt><dd>Nadia Ferrington</dd>
      <dt>Phone</dt><dd>(08) 6200 4471</dd>
      <dt>Mobile</dt><dd>0437255918</dd>
      <dt>Postal</dt><dd>48 Harbour Vale Rd Cottesby WA</dd>
      <dt></dt><dd class="wrap">6020 Australia</dd>
      <dt class="gap">Web</dt><dd class="gap">http://www.thebriskloft.com.au</dd>
      <dt>Email</dt><dd>info@thebriskloft.com.au</dd>
    </dl>
  </div>

  <form>
    <label class="abs form-label" style="top:513px">Your Name</label>
    <div class="abs form-field" style="top:508px"></div>
    <label class="abs form-label" style="top:544px">Your Email</label>
    <div class="abs form-field" style="top:539px"></div>
    <label class="abs form-label" style="top:574px">Phone Number</label>
    <div class="abs form-field" style="top:569px"></div>
    <label class="abs form-label" style="top:604px">Yor Company</label>
    <div class="abs form-field" style="top:600px"></div>
    <div class="abs form-message"><span>Type messege here....</span></div>
    <div class="abs btn-blue" style="left:694px;top:786px;width:79px;height:24px;line-height:24px">SUBMIT</div>
  </form>
</main>

<footer>
  <div class="abs social-icon" style="left:255px"></div>
  <div class="abs social-icon" style="left:291px"></div>
  <div class="abs social-icon" style="left:327px"></div>
  <div class="abs social-icon" style="left:364px"></div>
  <div class="abs social-icon" style="left:400px"></div>
  <p class="abs copyright">2011 © Copyright The Brisk Loft - Site map Phone: (08) 6200 4471 Australia</p>
</footer>
</body>
</html>
```